Larkmoor Heritage Guild Harvest Lantern Days Event Flyer - Historic Event

I need a flyer about the Larkmoor Heritage Guild's Harvest Lantern Days event October 8th and 9th. The centerpiece of Harvest Lantern Days is Civil War reenactments. I want the flyer to include the schedule of events and be eye catching on area bulletin boards. Our website is www.larkmoorheritageguild.org for more information and pictures. The website for the Tilden Rangers reenactors is http://www.tildenrangers.com/.

Target Market(s)

Our target market is middle ages (35-70) families and couples. Most are history buffs, especially about the Civil War.

Industry/Entity Type

Non-Profit

Font styles to use
Serif
Decorative
Script

Requirements
Must have
• The flyer must include the majority of the schedule attached - especially the battle times, museums, and anything including food.The dance on Saturday night is also important. The bottom of the flyer MUST say "Paid in part by Osgood County Visitor Fund Board"
Nice to have
• Pictures

```html
<!DOCTYPE html>
<html lang="en">
<head>
<meta charset="utf-8">
<title>Larkmoor Heritage Guild – Harvest Lantern Days Flyer</title>
<link rel="stylesheet" href="https://fonts.googleapis.com/css2?family=Cinzel:wght@500;700&family=Pinyon+Script&family=Roboto:wght@400;700&family=Roboto+Condensed:wght@700&family=Cormorant+Garamond:wght@500;700&display=swap">
<style>
  :root {
    --stage: #141414;
    --maroon: #6e1a12;
    --maroon-deep: #4a0f0a;
    --footer-red: #8a1111;
    --gold: #f1c94b;
    --cream: #f4ecd8;
    --ink: #333333;
    --accent-red: #a31212;
    --panel: #222427;
    --panel-text: #ffffff;
    --sunday-gold: #f5c518;
    --map: #e8df9a;
    --sepia: #6f5a45;
  }
  * { margin: 0; padding: 0; box-sizing: border-box; }
  html, body { width: 1200px; height: 960px; overflow: hidden; background: var(--stage); }
  .flyer {
    position: absolute; left: 249px; top: 26px; width: 706px; height: 908px;
    background: linear-gradient(160deg, #ffffff 0%, #f2f2f2 55%, #dcdcdc 100%);
    overflow: hidden;
  }
  .masthead {
    position: absolute; left: 0; top: 0; width: 100%; height: 94px;
    background: linear-gradient(180deg, var(--maroon) 0%, var(--maroon-deep) 100%);
    text-align: center; z-index: 3;
  }
  .masthead__title {
    position: absolute; top: 4px; width: 100%;
    font-family: "Cinzel", serif; font-weight: 700; font-size: 40px;
    color: var(--gold); letter-spacing: 0.5px;
  }
  .masthead__place {
    position: absolute; top: 50px; width: 100%;
    font-family: "Pinyon Script", cursive; font-size: 31px; color: var(--cream);
  }
  .photo-strip { position: absolute; left: 0; top: 78px; width: 100%; height: 239px; }
  .photo-strip__map-left { position: absolute; left: 0; top: 0; width: 158px; height: 100%;
    background: linear-gradient(90deg, #d9a86a 0%, var(--map) 30%, #efe7b5 100%); }
  .photo-strip__group { position: absolute; left: 158px; top: 0; width: 389px; height: 100%;
    background: radial-gradient(ellipse at 50% 70%, #8a7560 0%, var(--sepia) 55%, #3e3126 100%); }
  .photo-strip__map-right { position: absolute; left: 547px; top: 0; width: 159px; height: 100%;
    background: linear-gradient(90deg, #efe7b5 0%, var(--map) 60%, #d8c98a 100%); }
  .sunday-panel { position: absolute; left: 396px; top: 560px; width: 310px; height: 290px; background: var(--panel); }
  .feature-photo { position: absolute; left: 0; top: 0; z-index: 2; }
  .details { position: absolute; left: 24px; z-index: 4; font-family: "Roboto", sans-serif; font-size: 13.6px; color: var(--ink); white-space: nowrap; }
  .event-title { position: absolute; left: 24px; top: 336px; z-index: 4;
    font-family: "Cinzel", serif; font-weight: 700; font-size: 24px; color: var(--accent-red); white-space: nowrap; }
  .day-heading { font-family: "Roboto", sans-serif; font-weight: 700; font-size: 16px; text-decoration: underline; }
  .day-heading--sat { color: var(--accent-red); }
  .sponsor { font-family: "Roboto Condensed", sans-serif; font-weight: 700; font-size: 13px; color: #2a2a2a; }
  .sunday { position: absolute; left: 430px; z-index: 4; font-family: "Roboto", sans-serif; font-size: 13.6px; color: var(--panel-text); white-space: nowrap; line-height: 16px; }
  .sunday--heading { left: 421px; color: var(--sunday-gold); }
  .footer { position: absolute; left: 0; top: 850px; width: 100%; height: 58px;
    background: linear-gradient(90deg, var(--footer-red) 0%, var(--footer-red) 70%, #3a0b08 100%);
    font-family: "Cormorant Garamond", serif; font-weight: 500; font-size: 15px; color: #ffffff;
    text-align: center; line-height: 17px; padding-top: 4px; z-index: 4; }
  .footer__credit { font-weight: 700; color: var(--gold); }
</style>
</head>
<body>
<main class="flyer">
  <header class="masthead">
    <h1 class="masthead__title">Larkmoor Heritage Guild</h1>
    <p class="masthead__place">Larkmoor, Nebraska</p>
  </header>

  <section class="photo-strip">
    <div class="photo-strip__map-left" role="img" aria-label="Antique territorial map with rivers"></div>
    <div class="photo-strip__group" role="img" aria-label="Sepia photograph of a group of soldiers posed in a forest"></div>
    <div class="photo-strip__map-right" role="img" aria-label="Antique territorial map with lake region"></div>
  </section>

  <div class="sunday-panel"></div>

  <svg class="feature-photo" width="706" height="908" viewBox="0 0 706 908">
    <defs>
      <linearGradient id="wagonTones" x1="0" y1="0" x2="0" y2="1">
        <stop offset="0" stop-color="#c7a15a"/>
        <stop offset="0.45" stop-color="#d8d2c4"/>
        <stop offset="1" stop-color="#7a5a3a"/>
      </linearGradient>
      <linearGradient id="cabinTones" x1="0" y1="0" x2="0" y2="1">
        <stop offset="0" stop-color="#6f8f3e"/>
        <stop offset="1" stop-color="#8a7358"/>
      </linearGradient>
    </defs>
    <circle cx="551" cy="439" r="240" fill="#1c1c1e"/>
    <circle cx="551" cy="439" r="226" fill="#5a1410"/>
    <g role="img" aria-label="Photograph of a covered wagon under construction with reenactors">
      <circle cx="560" cy="436" r="216" fill="url(#wagonTones)"/>
    </g>
    <circle cx="382" cy="598" r="64" fill="#ffffff"/>
    <g role="img" aria-label="Photograph of a small log cabin among trees">
      <circle cx="382" cy="598" r="60" fill="url(#cabinTones)"/>
    </g>
  </svg>

  <h2 class="event-title">Harvest Lantern Days</h2>

  <p class="details day-heading day-heading--sat" style="top:389px">Saturday, October 8th, 2016</p>
  <p class="details" style="top:419px">Through&nbsp;&nbsp; the&nbsp;&nbsp; Day&nbsp;&nbsp; –&nbsp;&nbsp; Demonstrations&nbsp;&nbsp; and</p>
  <p class="details" style="top:446px">Speakers in various locations</p>
  <p class="details" style="top:474px">10:00 AM – Battle by Tilden Rangers</p>
  <p class="details sponsor" style="top:502px;left:62px">Sponsored in part by Halvorsen General Stores</p>
  <p class="details" style="top:557px">11:30-1:00 – Chicken Biscuit Bake at Town Hall</p>
  <p class="details" style="top:584px">– Free Will Donation</p>
  <p class="details" style="top:611px">Afternoon – Trolley and Buggy Rides</p>
  <p class="details" style="top:639px">1:00-4:00 Museums Opens</p>
  <p class="details" style="top:666px">1:30-2:00 Birthday Cake on Whitcomb House Front Porch</p>
  <p class="details sponsor" style="top:694px;left:63px">Cake donated by Pantry Market - Osgood City</p>
  <p class="details" style="top:745px">2:00 Battle by Tilden Rangers</p>
  <p class="details" style="top:772px">3:00-Sightseeing Cruise on the Spirit of Larkmoor</p>
  <p class="details" style="top:799px">6:00-? Dance at Town Hall with Cinder Creek Band</p>
  <p class="details sponsor" style="top:826px;left:66px">Sponsored by Dr. Ellworth</p>

  <p class="sunday sunday--heading day-heading" style="top:654px">Sunday, October 9th, 2016</p>
  <p class="sunday" style="top:680px">• 12:30 PM Parade on Main Street</p>
  <p class="sunday" style="top:706px">• Afternoon – Buggy &amp; Trolley Rides</p>
  <p class="sunday" style="top:732px">• 1:00-4:00 Museums Open</p>
  <p class="sunday" style="top:758px">• 1:30 Battle by Tilden Rangers</p>
  <p class="sunday" style="top:784px">• 2:00- Pie Reception at Larkmoor<br>&nbsp;&nbsp;&nbsp;Depot and Railroad History Museum</p>
  <p class="sunday" style="top:826px">• 3:00-Sightseeing Cruise</p>

  <footer class="footer">
    <p class="footer__credit">Paid in part by Osgood County Visitor Fund Board</p>
    <p>Larkmoor Heritage Guild, Box 1, Larkmoor, NE 68999</p>
    <p>(402) 555-0147 info@larkmoorheritageguild.org</p>
  </footer>
</main>
</body>
</html>
```